Butcher shop

We have 2 butcher shops:

Shop 7, Ridgeway Court, Aberdeen NSW 2336
Ph 02 6519 4482

58 Partridge St, Scone NSW 2337
Ph 02 6538 2170

ABN 47 308 915 226

I would like this info on reverse of card and my personal info on front of card. I have a logo I would like to use also. Require a very smooth thick matte card, with colour both sides.

Front of card should say:

Lorna Tewsbury
Accounts

Ph 0427 615 903
E lornatewsbury@mailnest.example

Industry/Entity Type

Shop

Contact Information for Business Card

Lorna Tewsbury
Ph 0427 615 903

Logo Text

Tewsbury's Quality Meats

Logo styles of interest
Pictorial/Combination Logo
Requirements
Must have
• We use Century Gothic Font

```html
<!DOCTYPE html>
<html lang="en">
<head>
<meta charset="utf-8">
<title>Tewsbury's Quality Meats – Business Card</title>
<link rel="stylesheet" href="https://fonts.googleapis.com/css2?family=Questrial&display=swap">
<style>
  :root {
    --backdrop: #e6e6e6;
    --card-white: #ffffff;
    --brand-blue: #67c3d9;
    --ink: #111111;
    --rule: #555555;
  }
  * { margin: 0; padding: 0; box-sizing: border-box; }
  html, body {
    width: 1200px; height: 849px; overflow: hidden;
    background: var(--backdrop);
    font-family: "Questrial", "Century Gothic", sans-serif;
    color: var(--ink);
  }
  .canvas { position: relative; width: 1200px; height: 849px; }
  .card {
    position: absolute; top: 290px; width: 467px; height: 268px;
    border-radius: 14px;
  }
  .card--front { left: 97px; background: var(--card-white); }
  .card--back { left: 634px; background: var(--brand-blue); text-align: center; }

  .logo-tile {
    position: absolute; left: 36px; top: 60px; width: 149px; height: 149px;
    background: var(--brand-blue); border-radius: 8px;
    display: flex; flex-direction: column; align-items: center; justify-content: flex-end;
    padding-bottom: 28px;
  }
  .brand-name { line-height: 1.1; letter-spacing: -0.3px; }
  .logo-tile .brand-name { font-size: 19.5px; text-align: center; }

  .divider {
    position: absolute; left: 205px; top: 88px; width: 1px; height: 90px;
    background: var(--rule);
  }
  .contact { position: absolute; left: 219px; top: 78px; white-space: nowrap; }
  .contact__name { font-size: 26px; letter-spacing: 0.2px; line-height: 30px; }
  .contact__role { font-size: 14px; margin-top: 3px; }
  .contact__details { font-size: 13.5px; line-height: 14px; margin-top: 19px; }

  .card--back .brand-name { position: absolute; left: 0; right: 0; top: 85px; font-size: 35px; line-height: 38px; }
  .locations {
    position: absolute; left: 0; right: 0; top: 189px;
    font-size: 13.5px; line-height: 15.5px; letter-spacing: 0.1px;
  }
</style>
</head>
<body>
<main class="canvas">
  <section class="card card--front" aria-label="Front of card">
    <div class="logo-tile">
      <p class="brand-name">Tewsbury's<br>Quality Meats</p>
    </div>
    <span class="divider"></span>
    <div class="contact">
      <p class="contact__name">Lorna Tewsbury</p>
      <p class="contact__role">Accounts</p>
      <p class="contact__details">Ph 0427 615 903<br>E:lornatewsbury@mailnest.example</p>
    </div>
  </section>

  <section class="card card--back" aria-label="Back of card">
    <p class="brand-name">Tewsbury's<br>Quality Meats</p>
    <p class="locations">
      Shop 7, Ridgeway Court, Aberdeen NSW 2336,&nbsp; Ph 02 6519 4482<br>
      58 Partridge St, Scone NSW 2337,&nbsp; Ph 02 6538 2170<br>
      ABN 47 308 915 226
    </p>
  </section>
</main>
</body>
</html>
```